Business Card Design Project - IT Company

Kestrafield Information Technology Solutions
We are an Information Technology Company. We provide computer services to commercial companies. We would like a new card full color front and back with bleeding edge.
We have a logo that you can use or if you want to come up with a new logo that is fine too.
Our colors are mostly Maroon and black but be creative.
Sample Information
Brent R Okafor
4812 W Saguaro Ridge Drive
Suite 410
Cardon Springs, AZ 85327
O: 602.914.2037
C: 602.468.1290
24/7: 888.914.2037
bokafor@kestrafield.example
www.kestrafield.example
Target Market(s)
Business of all sizes
Industry/Entity Type
Computer
Requirements
Must have
- Bleeding edge
full color on both sides

```html
<!DOCTYPE html>
<html lang="en">
<head>
<meta charset="utf-8">
<title>Kestrafield Business Card</title>
<link rel="stylesheet" href="https://fonts.googleapis.com/css2?family=Arimo:wght@400;700&display=swap">
<style>
  :root {
    --backdrop: #1a1a1a;
    --paper: #f6f6f6;
    --paper-shade: #dedede;
    --maroon: #b5202a;
    --maroon-deep: #7d0f16;
    --ink-grey: #4a4a4a;
    --tag-grey: #7a7a7a;
    --divider: #2a2a2a;
    --white: #ffffff;
  }
  html, body {
    margin: 0;
    padding: 0;
    width: 1200px;
    height: 871px;
    overflow: hidden;
    background: var(--backdrop);
    font-family: "Arimo", Arial, sans-serif;
  }
  .canvas {
    position: relative;
    width: 1200px;
    height: 871px;
  }
  .card {
    position: absolute;
    left: 170px;
    top: 190px;
    width: 860px;
    height: 492px;
    overflow: hidden;
    background: var(--maroon);
  }
  .card-art {
    position: absolute;
    inset: 0;
  }
  .brand {
    position: absolute;
    left: 84px;
    top: 40px;
  }
  .brand-name {
    margin: 0;
    font-size: 50px;
    font-weight: 700;
    letter-spacing: 4px;
    color: var(--ink-grey);
    line-height: 1;
  }
  .brand-tagline {
    margin: 6px 0 0 2px;
    font-size: 19px;
    font-weight: 400;
    color: var(--tag-grey);
  }
  .holder-name {
    position: absolute;
    left: 84px;
    top: 148px;
    margin: 0;
    font-size: 32px;
    font-weight: 700;
    color: var(--maroon);
  }
  .address {
    position: absolute;
    left: 40px;
    top: 290px;
    margin: 0;
    font-style: normal;
    font-size: 22px;
    font-weight: 700;
    line-height: 36px;
    color: var(--white);
    letter-spacing: 0.5px;
  }
  .contacts {
    position: absolute;
    right: 40px;
    top: 290px;
    margin: 0;
    padding: 0;
    list-style: none;
    text-align: right;
    font-size: 22px;
    font-weight: 700;
    line-height: 36px;
    color: var(--white);
    letter-spacing: 1px;
  }
</style>
</head>
<body>
<main class="canvas">
  <section class="card">
    <svg class="card-art" width="860" height="492" viewBox="0 0 860 492" aria-hidden="true">
      <defs>
        <linearGradient id="redField" x1="0" y1="0" x2="1" y2="1">
          <stop offset="0" stop-color="var(--maroon)"/>
          <stop offset="1" stop-color="var(--maroon-deep)"/>
        </linearGradient>
        <linearGradient id="paperField" x1="0" y1="0" x2="0" y2="1">
          <stop offset="0" stop-color="var(--white)"/>
          <stop offset="1" stop-color="var(--paper-shade)"/>
        </linearGradient>
      </defs>
      <rect class="red-field" width="860" height="492" fill="url(#redField)"/>
      <path class="paper-field" d="M0,0 H860 V140 C700,190 560,240 400,250 C250,258 120,245 0,225 Z" fill="url(#paperField)"/>
      <path class="divider-line" d="M0,225 C120,245 250,258 400,250 C560,240 700,190 860,140" fill="none" stroke="var(--divider)" stroke-width="6"/>
    </svg>

    <div class="brand">
      <p class="brand-name">KESTRAFIELD</p>
      <p class="brand-tagline">Information Technology Solutions</p>
    </div>
    <h1 class="holder-name">Brent R Okafor</h1>

    <address class="address">
      4812 W Saguaro Ridge Drive<br>
      Suite 410<br>
      Cardon Springs, AZ 85327
    </address>

    <ul class="contacts">
      <li>O: 602.914.2037</li>
      <li>C: 602.468.1290</li>
      <li>24/7: 888.914.2037</li>
      <li>bokafor@kestrafield.example</li>
      <li>www.kestrafield.example</li>
    </ul>
  </section>
</main>
</body>
</html>
```